Covid19 Poster for workplaces

Create a poster on how to protect yourself from Corona virus at work.
We are a Staffwell Health company. We have just re-branded so we need to fit in with our brand. We like clean and fresh, slightly amusing is ok if it will draw attention but it's an important topic. A4 and A3 please.

Content:

Headline: Lower the risk of COVID 19 in the workplace.

BE WELL

Bring your own cup - don’t share cups and food.
Elbow tap instead of handshakes and kisses
Wash your hands often - with soap.
Elbow or tissues when you cough or sneeze then straight in the bin
Leave your face alone after touching shared surfaces
Leave your bugs at home if you’re feeling unwell.

Call health line if you have a cough, a high temperature and shortness of breath. 0800 472 9160

Based on recommendations from ZPK and QLN

Target Market(s)

Employees - so anyone

Other font styles liked:
• Use the closest font to the brand documents

Requirements
Should not have
• Clip art

```html
<!DOCTYPE html>
<html lang="en">
<head>
<meta charset="utf-8">
<title>Lower the risk of COVID 19 in the workplace</title>
<link rel="stylesheet" href="https://fonts.googleapis.com/css2?family=Poppins:wght@500;700;800&display=swap">
<style>
  :root {
    --teal: #1fadb4;
    --navy: #2b3990;
    --yellow: #ffd51f;
    --ink: #231f20;
    --white: #ffffff;
    --virus-red: #d9452f;
    --virus-pale: #e9e3ef;
  }
  * { margin: 0; padding: 0; box-sizing: border-box; }
  html, body { width: 849px; height: 1200px; overflow: hidden; background: var(--white); }
  .poster {
    position: relative;
    width: 849px;
    height: 1200px;
    font-family: "Poppins", sans-serif;
    overflow: hidden;
  }
  .brand-bar {
    position: absolute; left: 0; top: 0; width: 100%; height: 88px;
    background: var(--teal);
    display: flex; align-items: center; justify-content: center; gap: 12px;
  }
  .brand-mark {
    width: 34px; height: 34px; border-radius: 50%; background: var(--white);
  }
  .brand-name {
    color: var(--white); font-weight: 700; font-size: 22px; line-height: 24px;
  }
  .headline-band {
    position: absolute; left: 0; top: 88px; width: 100%; height: 152px;
  }
  .headline-art {
    position: absolute; inset: 0;
    background: linear-gradient(90deg, #b8374a 0%, #6c3c8c 9%, var(--navy) 20%, var(--navy) 80%, #6c3c8c 91%, #b8374a 100%);
  }
  .headline {
    position: relative; z-index: 1;
    color: var(--white); text-align: center;
    font-weight: 800; font-size: 49px; line-height: 58px;
    letter-spacing: -0.5px;
    padding-top: 18px;
    text-shadow: 0 2px 6px rgba(0,0,0,0.45);
  }
  .headline .highlight { color: var(--yellow); }
  .tips-area {
    position: absolute; left: 0; top: 240px; width: 100%; height: 810px;
  }
  .tips-art {
    position: absolute; inset: 0;
    background:
      linear-gradient(90deg, rgba(217,69,47,0.75) 0%, rgba(233,227,239,0.8) 9%, #ffffff 22%, #ffffff 78%, rgba(233,227,239,0.8) 91%, rgba(217,69,47,0.75) 100%);
  }
  .tips {
    position: relative; z-index: 1; list-style: none;
  }
  .tip {
    position: absolute; left: 0; width: 849px; text-align: center;
    color: var(--ink); font-weight: 700; font-size: 27px; line-height: 39px;
    letter-spacing: -0.3px;
    text-shadow: 0 0 6px #fff, 0 0 10px #fff;
  }
  .contact-bar {
    position: absolute; left: 0; top: 1050px; width: 100%; height: 64px;
    background: var(--teal);
    display: flex; align-items: center; justify-content: center; gap: 14px;
    color: var(--white); font-weight: 700; font-size: 41px;
  }
  .contact-bar svg { width: 30px; height: 30px; }
  .source-bar {
    position: absolute; left: 0; top: 1114px; width: 100%; height: 86px;
    background: var(--yellow);
    display: flex; align-items: center; justify-content: center;
    color: var(--navy); font-weight: 500; font-size: 27px;
  }
</style>
</head>
<body>
<div class="poster">
  <header class="brand-bar">
    <span class="brand-mark"></span>
    <span class="brand-name">Staffwell<br>Health</span>
  </header>

  <section class="headline-band">
    <div class="headline-art" role="img" aria-label="Red and purple virus particle imagery framing the headline"></div>
    <h1 class="headline">LOWER THE RISK OF <span class="highlight">COVID 19</span><br>IN THE WORKPLACE</h1>
  </section>

  <section class="tips-area">
    <div class="tips-art" role="img" aria-label="Pale virus particle imagery on red-tinted edges around a white centre"></div>
    <ul class="tips">
      <li class="tip" style="top:35px">BRING YOUR OWN CUP</li>
      <li class="tip" style="top:107px">DON’T SHARE CUPS AND FOOD</li>
      <li class="tip" style="top:179px">ELBOW TAP INSTEAD OF HANDSHAKES<br>AND KISSES</li>
      <li class="tip" style="top:290px">WASH YOUR HANDS OFTEN – WITH SOAP</li>
      <li class="tip" style="top:361px">ELBOW OR TISSUES WHEN YOU COUGH OR<br>SNEEZE THEN STRAIGHT IN THE BIN</li>
      <li class="tip" style="top:471px">LEAVE YOUR FACE ALONE AFTER<br>TOUCHING SHARED SURFACES</li>
      <li class="tip" style="top:582px">LEAVE YOUR BUGS AT HOME IF YOU’RE<br>FEELING UNWELL</li>
      <li class="tip" style="top:691px">CALL HEALTH LINE IF YOU HAVE A COUGH A HIGH<br>TEMPERATURE AND SHORTNESS OF BREATH</li>
    </ul>
  </section>

  <div class="contact-bar">
    <svg viewBox="0 0 24 24" aria-hidden="true"><path fill="#ffffff" d="M6.6 10.8c1.4 2.8 3.8 5.1 6.6 6.6l2.2-2.2c.3-.3.7-.4 1-.2 1.1.4 2.3.6 3.6.6.6 0 1 .4 1 1V20c0 .6-.4 1-1 1C10.6 21 3 13.4 3 4c0-.6.4-1 1-1h3.5c.6 0 1 .4 1 1 0 1.3.2 2.5.6 3.6.1.3 0 .7-.2 1z"/></svg>
    <span class="phone">0800 472 9160</span>
  </div>

  <footer class="source-bar">Based on recommendations from ZPK and QLN</footer>
</div>
</body>
</html>
```